Re-design my 1-page website to be BETTER!

Hi Guys,
I recently created a 1-page website for market testing purposes for a company I am starting. Problem is, the feedback i've had on the page is its a bit corporate and boring.
I would love you to design something that is fresher, more modern and will generate leads (via the sign up CTA's).
Here is the website as it is now: www.guidelinkhub.com.au.
If you need any info or have questions, just reach out.
Thanks,
Oliver

Target Market(s)

Entrepreneurs

Number of Pages Required

1 page

Font styles to use
Sans Serif

Colors
abd036
34a6d7
ffffff

Requirements
Must have
• Fresh, Modern, high-converting
• I expect 70% of traffic to be mobile so must be mobile optimised first.
Nice to have
• I've highlighted colours i like below, however, I am open to suggestions. I like colours that are gender neutral and show energy and vibrancy.
• I have used Proxima Nova for the fonts, as I find it easy to read however, I am open to suggestions. My main preference is that it displays well and is easily read

```html
<!DOCTYPE html>
<html lang="en">
<head>
<meta charset="utf-8">
<title>GuideLink Hub – A Mentor For Everyone</title>
<link rel="stylesheet" href="https://fonts.googleapis.com/css2?family=Poppins:wght@400;500;600;700&family=Montserrat:wght@400;500;600&family=Roboto+Mono:wght@400;500&display=swap">
<style>
  :root {
    --green: #abd036;
    --blue: #34a6d7;
    --blue-deep: #1b9fcf;
    --band: #13a3cd;
    --ink: #2b2b2b;
    --body: #3c4a5c;
    --muted: #555;
    --soft: #f5f5f5;
    --white: #ffffff;
    --rule: #e2e2e2;
  }
  * { box-sizing: border-box; margin: 0; padding: 0; }
  html, body { width: 1200px; height: 3825px; overflow: hidden; }
  body { position: relative; background: var(--white); font-family: "Montserrat", sans-serif; color: var(--body); }
  .abs { position: absolute; }
  .center { left: 0; width: 1200px; text-align: center; }

  .btn {
    position: absolute; display: flex; align-items: center; justify-content: center;
    height: 42px; border-radius: 21px; color: var(--white);
    font-family: "Poppins", sans-serif; font-weight: 600; font-size: 13px; letter-spacing: .2px;
    text-transform: uppercase; text-decoration: none;
  }
  .btn--green { background: var(--green); }
  .btn--blue { background: var(--blue-deep); }
  .btn-note { font-size: 12px; color: var(--ink); }

  /* Hero */
  .hero { top: 0; left: 0; width: 1200px; height: 523px;
    background: linear-gradient(100deg, #7d7a70 0%, #5d5c55 35%, #4b5160 65%, #3b4350 100%); }
  .hero__brand { top: 66px; font-family: "Poppins", sans-serif; font-weight: 700; font-size: 44px; color: var(--green); letter-spacing: .5px; }
  .hero__tag { top: 128px; font-size: 17px; color: var(--white); letter-spacing: .5px; }
  .hero__points { top: 332px; font-size: 14px; color: var(--white); }
  .hero__points span { margin: 0 10px; }

  /* Quote */
  .quote { top: 523px; left: 0; width: 1200px; height: 231px; background: var(--soft); }
  .quote__text { top: 62px; left: 310px; width: 580px; text-align: center; font-family: "Roboto Mono", monospace; font-size: 14.5px; line-height: 18px; color: var(--ink); }
  .quote__mark { font-family: "Poppins", sans-serif; font-weight: 700; font-size: 46px; color: #111; line-height: 1; }
  .quote__rule { top: 140px; left: 312px; width: 576px; height: 1px; background: #ccc; }
  .quote__name { top: 156px; font-family: "Roboto Mono", monospace; font-size: 14px; color: var(--ink); }
  .quote__role { top: 176px; font-family: "Roboto Mono", monospace; font-size: 11px; color: var(--ink); }

  /* Finding */
  .finding__photo { top: 832px; left: 146px; width: 245px; height: 292px;
    background: linear-gradient(135deg, #2f6f9f 0%, #3c88b8 45%, #25557d 100%); }
  .finding__title { top: 828px; left: 615px; font-family: "Poppins", sans-serif; font-weight: 600; font-size: 28px; line-height: 30px; color: var(--blue-deep); }
  .finding__copy { top: 898px; left: 615px; width: 430px; font-size: 12.5px; line-height: 17.5px; color: var(--body); }
  .finding__copy p { margin-bottom: 17px; }
  .divider { top: 1265px; left: 131px; width: 938px; height: 1px; background: var(--rule); }

  /* Mentorship */
  .accent { height: 6px; width: 66px; background: var(--green); }
  .mentorship__title { top: 1354px; font-family: "Poppins", sans-serif; font-weight: 600; font-size: 27px; color: var(--blue-deep); }
  .mentorship__title em { font-style: normal; color: var(--green); }
  .mentorship__lead { top: 1404px; font-size: 14px; line-height: 18px; color: var(--ink); }
  .step { top: 1560px; width: 230px; text-align: center; }
  .step__icon { height: 96px; display: flex; align-items: center; justify-content: center; }
  .step__title { margin-top: 22px; font-weight: 600; font-size: 13.5px; color: var(--blue-deep); }
  .step__text { margin-top: 12px; font-size: 11.5px; line-height: 17.5px; color: var(--ink); }
  .step__bar { top: 1811px; width: 56px; height: 5px; background: var(--green); }

  /* Growth */
  .growth { top: 2006px; left: 0; width: 1200px; height: 694px; background: var(--band); }
  .growth__title { top: 2044px; font-family: "Poppins", sans-serif; font-weight: 600; font-size: 27px; color: var(--white); }
  .card { width: 293px; height: 208px; background: var(--white); text-align: center; padding: 26px 28px 0; }
  .card__title { font-weight: 500; font-size: 17px; color: var(--blue-deep); }
  .card__text { margin-top: 18px; font-size: 11px; line-height: 17.5px; color: var(--muted); }
  .growth__note { top: 2648px; font-size: 12.5px; color: var(--white); }

  /* FAQ */
  .faq__title { top: 2758px; font-family: "Poppins", sans-serif; font-weight: 600; font-size: 28px; color: var(--ink); }
  .faq { top: 2818px; left: 160px; width: 878px; height: 345px; background: var(--white); box-shadow: 0 0 12px rgba(0,0,0,.15); }
  .faq__list { position: absolute; top: 40px; left: 21px; width: 312px; list-style: none; }
  .faq__item { height: 31px; margin-bottom: 6px; border: 1px solid #eee; display: flex; align-items: center; padding-left: 12px; font-size: 13px; color: var(--ink); }
  .faq__item::before { content: ""; width: 7px; height: 7px; border: 1px solid #777; border-radius: 50%; margin-right: 11px; }
  .faq__item--active { color: var(--blue-deep); }
  .faq__item--active::before { background: var(--blue-deep); border-color: var(--blue-deep); }
  .faq__line { position: absolute; top: 20px; left: 368px; width: 2px; height: 300px; background: var(--blue-deep); }
  .faq__arrow { position: absolute; top: 44px; left: 370px; }
  .faq__answer { position: absolute; top: 44px; left: 401px; width: 450px; }
  .faq__q { display: inline-block; font-weight: 500; font-size: 18px; color: var(--blue-deep); border-bottom: 2px solid var(--blue-deep); padding-bottom: 2px; }
  .faq__a { margin-top: 18px; font-size: 11.5px; line-height: 14px; color: var(--body); }
  .faq__a p { margin-bottom: 13px; }

  /* Invest */
  .invest { top: 3231px; left: 0; width: 1200px; height: 594px;
    background: linear-gradient(180deg, #eef5fb 0%, #e4eef6 40%, #d9c2b0 75%, #c9a48c 100%); }
  .invest__title { top: 3302px; font-size: 27px; color: var(--ink); letter-spacing: .5px; }
  .invest__title span { background: var(--blue-deep); color: var(--white); padding: 2px 8px; }
  .invest__text { font-size: 12.5px; line-height: 17px; color: var(--ink); }
</style>
</head>
<body>

  <!-- Hero -->
  <header class="hero abs" role="img" aria-label="Blurred photo of a man in a shirt standing before a meeting room of seated colleagues"></header>
  <div class="hero__brand abs center">GUIDELINK HUB</div>
  <div class="hero__tag abs center">A MENTOR FOR EVERYONE</div>
  <div class="hero__points abs center">Free Registration.<span>|</span>100% Confidential.<span>|</span>100% Obligation Free</div>
  <a class="btn btn--blue" style="top:380px;left:510px;width:180px;">Find my mentor</a>

  <!-- Quote -->
  <section class="quote abs"></section>
  <div class="quote__mark abs" style="top:566px;left:278px;">&ldquo;</div>
  <p class="quote__text abs" style="top:585px;">We've flipped the model on its head - so now you choose your Mentor. It's never been this easy to get the advice and guidance you need to thrive.</p>
  <div class="quote__mark abs" style="top:607px;left:843px;">&rdquo;</div>
  <div class="quote__rule abs" style="top:663px;"></div>
  <svg class="abs" style="top:662px;left:595px;" width="10" height="6"><path d="M0 0 L5 5 L10 0" fill="#ccc"/></svg>
  <div class="quote__name abs center" style="top:679px;">Oliver,</div>
  <div class="quote__role abs center" style="top:700px;">Founder - GuideLink Hub</div>

  <!-- Finding a mentor -->
  <div class="finding__photo abs" role="img" aria-label="Blue jigsaw puzzle with one lifted piece"></div>
  <h2 class="finding__title abs">Finding a Mentor<br>Has Never Been Easier</h2>
  <div class="finding__copy abs">
    <p>Having a great Mentor will turbo-charge your personal, professional or business growth. But unless you have an incredible network, finding great Mentors has always been a challenge.</p>
    <p>GuideLink Hub changes all that, levelling the playing field and making it easy for entrepreneurs and professionals to find the advice and guidance they deserve.</p>
    <p>No longer will you have to go searching for your perfect Mentor. We bring the perfect Mentor to you, selected from a global pool of experts, putting the power back in your hands and letting you get on with your growth.</p>
  </div>
  <a class="btn btn--green" style="top:1172px;left:508px;width:184px;">Let's get started</a>
  <div class="btn-note abs center" style="top:1227px;">Register Free. 100% confidential. Obligation Free</div>
  <div class="divider abs"></div>

  <!-- Mentorship but different -->
  <div class="accent abs" style="top:1330px;left:567px;"></div>
  <h2 class="mentorship__title abs center">MENTORSHIP : BUT <em>DIFFERENT</em></h2>
  <p class="mentorship__lead abs center">Finding a Mentor used to be hard; but not any more. We've turned the traditional model<br>on its head, so now Mentors seek you.</p>
  <svg class="abs" style="top:1452px;left:280px;" width="640" height="104" viewBox="0 0 640 104" fill="none" stroke="#1f3f6e" stroke-width="1.3">
    <path d="M320 0 V100 M8 66 H632 M8 66 V100 M632 66 V100"/>
    <path d="M4 95 L8 101 L12 95 M316 95 L320 101 L324 95 M628 95 L632 101 L636 95"/>
  </svg>

  <div class="step abs" style="left:178px;">
    <div class="step__icon">
      <svg width="100" height="90" viewBox="0 0 100 90"><path d="M4 4 H96 V58 H30 L16 76 V58 H4 Z" fill="#1d9bd1" rx="6"/><circle cx="28" cy="31" r="5" fill="#fff"/><circle cx="48" cy="31" r="5" fill="#fff"/><circle cx="68" cy="31" r="5" fill="#fff"/></svg>
    </div>
    <div class="step__title">Tell Us What You Need</div>
    <p class="step__text">There is no one size fits all approach to Mentorship. So tell us the challenges you are facing and the skill-set your Mentor must have.</p>
  </div>
  <div class="step abs" style="left:485px;">
    <div class="step__icon">
      <svg width="80" height="88" viewBox="0 0 80 88"><circle cx="40" cy="20" r="19" fill="#1d9bd1"/><path d="M2 88 C2 58 16 44 40 44 C64 44 78 58 78 88 Z" fill="#1d9bd1"/><path d="M33 44 L40 52 L47 44 Z M40 52 L36 80 L40 86 L44 80 Z" fill="#fff"/></svg>
    </div>
    <div class="step__title">Choose Your Mentor</div>
    <p class="step__text">Mentors are invited to Mentor you. We select 3 top picks that align with your criteria. It's then up to you whether you choose a Mentor, interview 1 or more or refine your criteria and start again.</p>
  </div>
  <div class="step abs" style="left:797px;">
    <div class="step__icon">
      <svg width="140" height="60" viewBox="0 0 140 60"><path d="M2 8 L22 4 L28 44 L8 48 Z M138 8 L118 4 L112 44 L132 48 Z" fill="#1d9bd1"/><path d="M30 12 L56 8 L78 18 L92 10 L110 14 L106 42 L80 58 L60 52 L32 40 Z" fill="#1d9bd1"/><path d="M56 30 L72 40 M62 24 L80 36 M70 20 L88 32" stroke="#fff" stroke-width="2.5" stroke-linecap="round"/></svg>
    </div>
    <div class="step__title">Ongoing Support</div>
    <p class="step__text">We don't stop once you have your perfect Mentor. We're on hand to make life easy for you, keep your sessions on track and provide ongoing support.</p>
  </div>
  <div class="step__bar abs" style="left:265px;"></div>
  <div class="step__bar abs" style="left:572px;"></div>
  <div class="step__bar abs" style="left:884px;"></div>

  <a class="btn btn--green" style="top:1871px;left:508px;width:184px;">Register for free</a>
  <div class="btn-note abs center" style="top:1927px;">100% confidential and 100% obligation free.</div>

  <!-- Growth -->
  <section class="growth abs"></section>
  <h2 class="growth__title abs center">How a Mentor Will Accelerate Your Growth</h2>
  <div class="card abs" style="top:2113px;left:146px;"><div class="card__title">Impartial advice</div><p class="card__text">Imagine being able to speak to someone who has been through the challenges you are currently facing? Who has "been there seen that" and can help you navigate the ups and downs of your career or business?</p></div>
  <div class="card abs" style="top:2113px;left:453px;"><div class="card__title">Avoid the Pitfalls</div><p class="card__text">An experienced Mentor will help you see the challenges before they arise and make sure you avoid them altogether. Saving valuable time and money in the process.</p></div>
  <div class="card abs" style="top:2113px;left:760px;padding-top:22px;"><div class="card__title">A Supportive Ear</div><p class="card__text" style="margin-top:14px;">Running a business and the challenges of corporate life can be extremely stressful. And often, our friends and family just don't get it. So imagine having someone independent who can understand where your coming from and, help you see things objectively.</p></div>
  <div class="card abs" style="top:2339px;left:146px;"><div class="card__title">Clarity</div><p class="card__text">Sometimes we are so caught up in our own world we struggle to see the big picture. You Mentor will provide an objective, outsider view. Helping you to cut though the noise and focus on what's really important.</p></div>
  <div class="card abs" style="top:2339px;left:453px;"><div class="card__title">Motivation</div><p class="card__text">Your Mentor has seen this before and been in your shoes. They understand what your going through and will help you to re-focus and re-energise.</p></div>
  <div class="card abs" style="top:2339px;left:760px;padding-top:30px;"><div class="card__title">Make you Accountable</div><p class="card__text">A Mentor is not just there to pick you up - they are to give honest appraisal and tell you when your falling short. Ultimately, only you can control your success and you Mentor will hold you accountable to make sure you are.</p></div>
  <a class="btn btn--green" style="top:2593px;left:508px;width:184px;">Register now</a>
  <div class="growth__note abs center">Your closer to your perfect mentor than you think. Register today to see how easy it can be.</div>

  <!-- FAQ -->
  <h2 class="faq__title abs center">Frequently Asked Questions</h2>
  <section class="faq abs">
    <ul class="faq__list">
      <li class="faq__item faq__item--active">What is a Mentor?</li>
      <li class="faq__item">Is a Mentor right for me?</li>
      <li class="faq__item">How often do we meet?</li>
      <li class="faq__item">Can I have more than one Mentor?</li>
      <li class="faq__item">What if it doesn't work out?</li>
      <li class="faq__item">How do we meet?</li>
      <li class="faq__item">What are the costs?</li>
    </ul>
    <div class="faq__line"></div>
    <svg class="faq__arrow" width="10" height="18"><path d="M0 0 L10 9 L0 18 Z" fill="var(--blue-deep)"/></svg>
    <div class="faq__answer">
      <div class="faq__q">What is a Mentor?</div>
      <div class="faq__a">
        <p>Experienced and Trusted Advisor. Guru. Confidente. Friend.</p>
        <p>In essence a Mentor is someone who can turn to for guidance and advice.</p>
        <p>Someone who is more experienced than you and, has navigated similar challenges to you and can foresee the pitfalls and hurdles you face.</p>
        <p>A great Mentor is also a motivator, connector and guide. Will help you focus on what's really important and see the bigger picture.</p>
        <p>Importantly, a great Mentor should be outside your immediate network of friends and relatives. And, be able to offer unbiased, honest and objective advice, that you can action.</p>
      </div>
    </div>
  </section>

  <!-- Invest -->
  <section class="invest abs" role="img" aria-label="Photo of two hands clasped in a handshake against a bright pale blue background"></section>
  <h2 class="invest__title abs center">IT'S TIME TO INVEST IN <span>YOU</span></h2>
  <p class="invest__text abs center" style="top:3364px;">If you've come this far you've already taken the most important step: recognising how<br>mentorship can help you; and taking action to find it.</p>
  <p class="invest__text abs center" style="top:3421px;">And now your here, the rest is easy.</p>
  <p class="invest__text abs center" style="top:3456px;"><strong>Get started now</strong> and let GuideLink Hub do the rest...</p>
  <a class="btn btn--blue" style="top:3521px;left:508px;width:184px;">Let's do this</a>
  <div class="invest__text abs center" style="top:3576px;">Sign up is free, obligation free and 100% confidential</div>

</body>
</html>
```